Gentle Willow Pregnancy and Baby Massage

I need a web design for a new business, GENTLE WILLOW PREGNANCY AND BABY MASSAGE that I am in the process of setting up in the suburbs of Perth, Western Australia. The business is owned and operated by myself and my intention is to service Pregnant Mothers and Parents of Young Babies that would benefit from massage. I would like to have a "Home Page" and pages for "About Me", "Pregnancy Massage", "Baby Massage", a Pricing Page for Pregnancy Massage Sessions, a Pricing Page for Baby Massage Sessions, and a "Contact Me" page to allow clients to either contact me with queries or book available pregnancy massage sessions on a particular day of the week. I would also like a "News" page that would include articles I have written, news about new courses and a link to my Chatterlane page (yet to be set up). I would like to keep the colour schemes similar to my logo design colours. I need the design to be easy to follow and to appeal to a younger audience (20's to mid 30's).
The target audience is pregnant mothers-to-be wishing to receive massage treatments, and new parents and grandparents of small babies that would like to learn how to massage their babies.
The look and feel should be modern, professional, elegant and feminine.
I need the design to be in a standard format such that I can update the content by myself ( and does not need specialised software) as the company and business progresses.

Target Market(s)

Industry/Entity Type

Health And Wellness

Contact Information for Business Card

Card should have rounded edges. Design should have the same "feel" as the website. Contact Details of my business address, mobile phone, email and website should be included.

Coding

Coded - Design and coding required

Number of Pages Required

5+ page

Font styles to use
Script

Requirements
Must have
• Same colours as logo design. In cmyk system, the colours are: 20,60,0,0 which best result is tintora 681 and 40,40,0,0 which best result is tintora 2645. Card should include the logo design.

```html
<!DOCTYPE html>
<html lang="en">
<head>
<meta charset="utf-8">
<title>Pregnancy Massage – Gentle Willow Pregnancy and Baby Massage</title>
<link href="https://fonts.googleapis.com/css2?family=Montserrat:wght@400;500&family=Open+Sans:wght@400&display=swap" rel="stylesheet">
<style>
:root{
  --band:#a29bc7;
  --pink:#b660a4;
  --lilac:#9d95c8;
  --ink:#4a4a4a;
  --body:#666;
  --page:#f6f6f6;
  --footer:#ececec;
  --muted:#8c8c8c;
  --icon:#c8c8c8;
}
*{margin:0;padding:0;box-sizing:border-box}
html,body{width:785px;height:1200px;overflow:hidden;background:var(--page)}
body{position:relative;font-family:"Open Sans",sans-serif;color:var(--ink)}
.top-band{position:absolute;left:0;top:0;width:785px;height:54px;background:var(--band)}
.menu-toggle{position:absolute;left:666px;top:21px;width:21px}
.menu-toggle span{display:block;height:2px;background:#fff;margin-bottom:3.5px}
.brand-tab{position:absolute;left:96px;top:0;width:180px;height:116px}
.brand-tab svg{position:absolute;left:0;top:0}
.brand-name{position:absolute;left:0;top:30px;width:180px;text-align:center;font-family:"Montserrat",sans-serif;font-weight:500;color:var(--pink);font-size:17px;line-height:1.1}
.brand-name small{display:block;font-size:10.5px;margin-top:4px}
.brand-dot{position:absolute;left:80px;top:8px;width:18px;height:18px;border-radius:50%;background:var(--pink)}
.content{position:absolute;left:96px;top:124px;width:592px}
h1{font-family:"Montserrat",sans-serif;font-weight:400;font-size:21px;color:#555;margin-bottom:6px}
.lead{font-size:10.5px;line-height:16px;color:var(--body)}
.source{font-family:"Montserrat",sans-serif;font-style:italic;font-size:11px;color:var(--pink);margin-top:6px}
h2{font-family:"Montserrat",sans-serif;font-weight:400;color:var(--pink)}
.benefits-title{font-size:19px;margin-top:14px}
.benefits-title span{color:var(--lilac)}
.hero{width:592px;height:295px;margin-top:7px;background:linear-gradient(100deg,#e6e4e2 0%,#d9b59a 42%,#d6ab8c 62%,#ecebea 80%,#e2e1e0 100%)}
.section-title{font-size:16.5px;margin-top:21px;margin-bottom:10px}
ul{list-style:none}
.points li{font-size:8.4px;line-height:17.5px;color:#444}
.points li::before{content:"• "}
.note{font-size:8.6px;line-height:14.5px;color:var(--body)}
h3{font-family:"Montserrat",sans-serif;font-weight:500;font-size:11.5px;color:#333;margin:9px 0 8px}
.gap{margin-top:12px}
.site-footer{position:absolute;left:0;top:1078px;width:785px;height:122px;background:var(--footer)}
.badge{position:absolute;left:104px;top:20px;width:76px;height:92px;border:1.5px solid var(--pink);border-radius:38px 38px 6px 6px}
.cert{position:absolute;left:188px;top:14px;font-family:"Montserrat",sans-serif;font-size:15px;line-height:19.5px;color:var(--muted)}
.cert span{color:var(--pink)}
.footer-head{position:absolute;font-family:"Montserrat",sans-serif;font-size:13.5px;color:var(--pink);top:14px}
.links{position:absolute;top:40px;font-size:7.6px;line-height:16.8px;color:#777}
.socials{position:absolute;left:572px;top:39px;display:flex;gap:7px}
.socials span{width:20px;height:20px;border-radius:50%;background:var(--icon)}
.copy{position:absolute;left:572px;top:70px;font-size:7.4px;color:#777}
</style>
</head>
<body>
<header>
  <div class="top-band"></div>
  <div class="brand-tab">
    <svg width="180" height="116" viewBox="0 0 180 116"><path d="M0 0H180V100L90 116L0 100Z" fill="#fff"/></svg>
    <span class="brand-dot"></span>
    <div class="brand-name">Gentle Willow<small>Pregnancy and Baby Massage</small></div>
  </div>
  <div class="menu-toggle" aria-label="Menu"><span></span><span></span><span></span></div>
</header>

<main class="content">
  <h1>Pregnancy Massage</h1>
  <p class="lead">Pregnancy massage is the prenatal use of massage therapy to support the physiological, structural and emotional wellbeing of both mother and baby.</p>
  <p class="source">Source: Bloomwell Pregnancy Massage Australia</p>

  <h2 class="benefits-title">Benefits of <span>Pregnancy Massage</span></h2>
  <div class="hero" role="img" aria-label="Photo of a therapist's hands gently massaging a pregnant belly, towels draped around"></div>

  <h2 class="section-title">Pregnancy Massage is a professional relaxation massage that:</h2>
  <ul class="points">
    <li>Reduces anxiety caused by hormonal changes</li>
    <li>Improves circulation</li>
    <li>Reduces muscle aches and pain; muscle and joint conditions such as backache, shoulder and neck pain, hip pain, leg cramps, oedema and carpel tunnel</li>
    <li>Relaxes tense muscle, tones loose muscle and increases muscle flexibility.</li>
    <li>Enhances vitality and energy</li>
    <li>Reduces fatigue</li>
    <li>Enhances relaxation and improves sleep patterns as it helps to soothe and relax nervous tension</li>
    <li>Increases circulation to the skin</li>
  </ul>

  <h2 class="section-title">Is Pregnancy Massage Safe?</h2>
  <p class="note">Yes, when the massage is performed by a qualified pregnancy massage therapist, who is aware of your medical and obstetric history. It is recommended to align your massage for just after your ante natal check, so that up to date information is available.</p>
  <h3>There are times when pregnancy massage is not appropriate.</h3>
  <ul class="points">
    <li>The abdomen will not be massaged during the first trimester.</li>
    <li>It is recommended to wait at least one week after amniocentesis, or any invasive procedures.</li>
    <li>If you have a history of blood clots in the legs, any vaginal bleeding, or cramping, pregnancy massage is not recommended.</li>
  </ul>
  <p class="note gap">Certain medical or obstetric conditions will require medical clearance from your obstetrician.</p>
  <h3>These include;</h3>
  <ul class="points">
    <li>Unstable or high blood pressure</li>
    <li>Heart disease</li>
    <li>Placenta praevia</li>
    <li>Cervical incompetence</li>
  </ul>
</main>

<footer class="site-footer">
  <div class="badge" role="img" aria-label="Certification badge"></div>
  <p class="cert">Certified by<br><span>gentle</span><br><span>touch</span><br>learning<br>network</p>

  <div class="footer-head" style="left:309px">Quick Links</div>
  <ul class="links" style="left:310px">
    <li>Home</li><li>About Me</li><li>Benefits of Pregnancy</li><li>Benefits of Baby Massage</li>
  </ul>
  <ul class="links" style="left:433px">
    <li>Pregnancy Massage Sessions</li><li>Baby Massage Sessions</li><li>Contact</li>
  </ul>

  <div class="footer-head" style="left:574px">Follow Us</div>
  <div class="socials" aria-label="Social links"><span></span><span></span><span></span><span></span></div>
  <p class="copy">© 2017 Gentle Willow Pregnancy</p>
</footer>
</body>
</html>
```